Business card design needed

I am a business consultant but I call myself an "organizational leadership consultant." My clients hire me to do organizational development work in the areas of leadership development, strategic planning, shared visioning, governance (bylaws, policy, board development), collaborative capacity building, and organizational communications. I work in numerous sectors (public, private, not-for-profit and governmental) but most of my clients are in not-for-profit (but not human service - think national advocacy organizations, student governments, regulatory colleges, and professional (accreditation) bodies).

I want my cards to convey the concepts of being reliable and smart (of course) but also vibrant and signifying new beginnings/possibilities.

I am uploading a copy of a logo I have used for some time (adapted from QV logo free website). I like the hues of the primary colours used, its symmetrical, and that it has movement. I am open to a new logo (but not essential) with these same qualities: I really like fractals BTW.

I think one of the most beautiful creatures on earth is the harlequin duck, but have not been able to figure out how to incorporate that into my brand. Mostly what I love is the colours and how they appear on the duck. I am sharing that just as an idea in case your creative energy is leaning toward creating a new design rather than working with my logo.

If I had the right business card to start with, I might consider re-branding and working that into my digital and print materials. I realize this is against the use of RGBY in my current logo.
Updates

Hi - I forgot to mention to please use the RTVP Certified patch/logo as a just a small feature of the card - it is not my main logo. Also, I like fonts that are clean.  Thanks!

Target Market(s)

Higher level business professionals

Industry/Entity Type

Business Consultant

Contact Information for Business Card

Moira Castellane, MA, BSc, RTVP(pls insert trademark symbol)
Organizational Leadership Consultant
250-487-6190
moira@mcastellaneadvisory.example
www.mcastellaneadvisory.example
Fernhollow Bay, BC

Logo Text

Leadership Consulting for a New Future

Logo styles of interest
Emblem Logo
Abstract Logo
Requirements
Must have
• Must have:
1. Name of my business (Moira Castellane Consulting) and contact info per above
2. My logo (or your new idea for a logo) with a my tagline somewhere (tagline can be on back. Tagline is "Leadership Consulting for a New Future)
3. RTVP certified logo (attachment #3)
3. Chirpline logo with my acct name (@moiracastellane), and
4. Workweave logo
Should not have
• I don't like the "solid" primary colours as in those found on brikko or in a poppets box - transparency in those colours is acceptable.

Do not include images of people shaking hands or other corny 'business' imagery.;-)

```html
<!DOCTYPE html>
<html lang="en">
<head>
<meta charset="utf-8">
<title>Moira Castellane Consulting – Business Card</title>
<link rel="stylesheet" href="https://fonts.googleapis.com/css2?family=Questrial&display=swap">
<style>
  :root {
    --stage: #2b2b2b;
    --card-top: #132320;
    --card-bottom: #0c1715;
    --ink: #d9dedc;
    --ink-soft: #aeb6b3;
    --accent-green: #7fb23a;
    --pebble-green: #2c4a35;
    --pebble-brown: #3a2e26;
    --badge-orange: #e8641e;
    --social: #4f9fc9;
  }
  * { margin: 0; padding: 0; box-sizing: border-box; }
  html, body { width: 1200px; height: 900px; overflow: hidden; }
  body {
    background: var(--stage);
    font-family: "Questrial", "Century Gothic", sans-serif;
    color: var(--ink);
    position: relative;
  }
  .card {
    position: absolute;
    width: 560px;
    height: 320px;
    left: 320px;
    background: linear-gradient(160deg, var(--card-top), var(--card-bottom));
    box-shadow: 0 10px 30px rgba(0,0,0,.5);
    overflow: hidden;
  }
  .card--front { top: 110px; }
  .card--back { top: 470px; }

  /* front */
  .brand-mark {
    position: absolute;
    right: 70px; top: 40px;
    width: 190px; height: 190px;
    border-radius: 50%;
    background: radial-gradient(circle, rgba(240,190,40,.85) 0%, rgba(120,190,70,.7) 30%, rgba(60,140,210,.55) 55%, rgba(40,180,190,.2) 75%, rgba(19,35,32,0) 100%);
  }
  .brand-name {
    position: absolute;
    left: 40px; bottom: 70px;
    font-size: 22px;
    letter-spacing: .5px;
    color: var(--ink);
  }
  .brand-tagline {
    position: absolute;
    left: 40px; bottom: 46px;
    font-size: 15px;
    color: var(--accent-green);
  }

  /* back */
  .pebbles {
    position: absolute;
    left: 0; top: 0;
    width: 180px; height: 320px;
    background: linear-gradient(200deg, rgba(44,74,53,.9) 0%, rgba(58,46,38,.7) 50%, rgba(44,74,53,.6) 100%);
    clip-path: polygon(0 0, 70% 0, 100% 40%, 70% 100%, 0 100%);
  }
  .cert-badge {
    position: absolute;
    left: 22px; top: 26px;
    width: 76px; height: 76px;
    background: var(--badge-orange);
    border-radius: 6px;
  }
  .details {
    position: absolute;
    right: 34px; top: 22px;
    text-align: right;
  }
  .credentials { font-size: 10px; color: var(--ink-soft); letter-spacing: 1px; }
  .person-name { font-size: 30px; font-weight: 400; letter-spacing: 2px; line-height: 1.05; }
  .person-title { font-size: 16px; color: var(--accent-green); margin-bottom: 22px; }
  .contact { list-style: none; font-size: 15px; line-height: 1.55; }
  .contact li.gap { margin-top: 10px; }
  .social { list-style: none; font-size: 11px; color: var(--ink-soft); margin-top: 12px; line-height: 1.7; }
  .social li { display: flex; justify-content: flex-end; align-items: center; gap: 6px; }
  .social-dot { width: 9px; height: 9px; background: var(--social); border-radius: 50%; }
  .social-square { width: 9px; height: 9px; background: var(--social); }
</style>
</head>
<body>
  <section class="card card--front">
    <div class="brand-mark" role="img" aria-label="Symmetrical fractal emblem in blue, green, yellow and red"></div>
    <p class="brand-name">Moira Castellane Consulting</p>
    <p class="brand-tagline">Leadership Consulting for a New Future</p>
  </section>

  <section class="card card--back">
    <div class="pebbles" role="img" aria-label="Translucent pebble-shaped pattern in green and brown"></div>
    <div class="cert-badge" role="img" aria-label="Certification badge"></div>
    <div class="details">
      <p class="credentials">MA, BSc, RTVP™</p>
      <h1 class="person-name">MOIRA CASTELLANE</h1>
      <p class="person-title">Organizational Leadership Consultant</p>
      <ul class="contact">
        <li>250-487-6190</li>
        <li>Fernhollow Bay, BC</li>
        <li class="gap">moira@mcastellaneadvisory.example</li>
        <li>www.mcastellaneadvisory.example</li>
      </ul>
      <ul class="social">
        <li>@moiracastellane <span class="social-dot" aria-label="Chirpline"></span></li>
        <li>workweave/moiracastellane <span class="social-square" aria-label="Workweave"></span></li>
      </ul>
    </div>
  </section>
</body>
</html>
```